carpet cleaning flyer/leaflet modern/upmarket twist

We are Velvet Nest, We do carpet & upholstery cleaning for the domestic market, if you are able to incorporate images like the ones I have provided that would be awesome, please feel free to find similar! mine are only examples. id like a front cover photo with the company name running through it, and the back to be half picture and then the detailing of what we do which is in the document I've uploaded
Target Market(s)
Domestic house hold
Industry/Entity Type
Cleaning Service
Colors
eea4c8
e667a6
c3c3c3
cbcbcb
aaaaaa
f59296
Requirements
Must have
- It must be 2 sided also have A modern but upmarket feel, a luxury. a front picture with name on it, back page with picture and writing from the word document.
Nice to have
- a input from yourselves, your twist on it

```html
<!DOCTYPE html>
<html lang="en">
<head>
<meta charset="utf-8">
<title>Velvet Nest – Carpet and Upholstery Cleaning Flyer</title>
<link href="https://fonts.googleapis.com/css2?family=Oswald:wght@500;600;700&family=Roboto:wght@500;700&family=Lato:wght@400;700&display=swap" rel="stylesheet">
<style>
  :root {
    --pink: #f06a8e;
    --pink-soft: #eea4c8;
    --ink: #1f1d1e;
    --ink-deep: #161515;
    --white: #ffffff;
    --page: #2a2a2a;
    --carpet-light: #8f867d;
    --carpet-mid: #6c635b;
    --carpet-dark: #3e3833;
  }
  * { margin: 0; padding: 0; box-sizing: border-box; }
  html, body { width: 900px; height: 1200px; overflow: hidden; }
  body { background: var(--page); position: relative; font-family: "Lato", sans-serif; }

  .card { position: absolute; overflow: hidden; }

  /* Front */
  .front { left: 107px; top: 70px; width: 693px; height: 498px; }
  .front-photo {
    position: absolute; inset: 0;
    background:
      radial-gradient(ellipse 60% 45% at 55% 45%, rgba(190,180,170,.45), transparent 70%),
      linear-gradient(160deg, var(--carpet-light) 0%, var(--carpet-mid) 45%, var(--carpet-dark) 100%);
  }
  .front-title {
    position: absolute; left: 50px; top: 105px;
    font-family: "Oswald", sans-serif; font-weight: 700; color: var(--pink);
    line-height: .9; text-transform: uppercase;
  }
  .front-title .line-1 { display: block; font-size: 132px; letter-spacing: 1px; }
  .front-title .line-2 { display: block; font-size: 88px; letter-spacing: 1px; }
  .front-tagline {
    position: absolute; left: 51px; top: 318px;
    font-family: "Roboto", sans-serif; font-weight: 700; font-size: 15px;
    color: var(--white); letter-spacing: .4px; text-transform: uppercase;
  }
  .front-contact-band {
    position: absolute; left: 0; right: 0; top: 423px; height: 40px;
    background: rgba(30,27,25,.72);
  }

  .contact {
    position: absolute; display: flex; align-items: center; gap: 6px;
    font-family: "Roboto", sans-serif; font-weight: 700; font-size: 20px;
  }
  .contact svg { width: 24px; height: 24px; flex: none; }
  .front .contact { color: var(--pink); top: 430px; }
  .front .contact-phone { left: 46px; }
  .front .contact-email { left: 316px; }

  /* Back */
  .back { left: 110px; top: 636px; width: 696px; height: 492px; background: var(--ink); }
  .back-photo {
    position: absolute; left: 330px; top: 0; width: 366px; height: 400px;
    background: linear-gradient(180deg, #6e4a33 0%, #5a4030 45%, #8a7868 75%, #a39684 100%);
  }
  .back-photo-fade {
    position: absolute; left: 330px; top: 0; width: 140px; height: 400px;
    background: linear-gradient(90deg, var(--ink) 0%, rgba(31,29,30,0) 100%);
  }
  .back-copy { position: absolute; left: 38px; top: 62px; width: 272px; }
  .feature { margin-bottom: 16px; }
  .feature-title {
    font-family: "Roboto", sans-serif; font-weight: 700; font-size: 16px;
    color: var(--pink); text-decoration: underline; text-underline-offset: 3px;
    text-transform: uppercase; margin-bottom: 6px;
  }
  .feature-text { font-size: 10.5px; line-height: 13px; color: var(--white); text-align: justify; }
  .back-name {
    position: absolute; left: 38px; top: 345px;
    font-family: "Oswald", sans-serif; font-weight: 600; font-size: 30px;
    color: var(--pink); text-transform: uppercase; letter-spacing: .3px;
  }
  .back-contact-band {
    position: absolute; left: 0; right: 0; top: 399px; height: 50px; background: var(--pink);
  }
  .back .contact { color: var(--ink-deep); top: 410px; font-size: 21px; }
  .back .contact-phone { left: 40px; }
  .back .contact-email { left: 310px; }
</style>
</head>
<body>

<section class="card front">
  <div class="front-photo" role="img" aria-label="Close-up photo of a vacuum cleaner head gliding over soft beige carpet, leaving a clean sweep"></div>
  <h1 class="front-title"><span class="line-1">Velvet</span><span class="line-2">Nest</span></h1>
  <p class="front-tagline">Carpet and Upholstery Cleaning</p>
  <div class="front-contact-band"></div>
  <p class="contact contact-phone">
    <svg viewBox="0 0 24 24" fill="none" stroke="currentColor" stroke-width="1.6"><circle cx="12" cy="12" r="10.5"/><path d="M8.5 6.5l2 2.2-1.1 1.6c.8 1.7 2 2.9 3.7 3.7l1.6-1.1 2.2 2-1.2 1.8c-4-.6-7.2-3.8-7.8-7.8z"/></svg>
    01632 960 418
  </p>
  <p class="contact contact-email">
    <svg viewBox="0 0 24 24" fill="none" stroke="currentColor" stroke-width="1.6"><circle cx="12" cy="12" r="10.5"/><rect x="6.5" y="8" width="11" height="8"/><path d="M6.5 8l5.5 4.5L17.5 8"/></svg>
    info@velvetnest-clean.co.uk
  </p>
</section>

<section class="card back">
  <div class="back-photo" role="img" aria-label="Photo of a warm modern living room with beige sectional sofa, orange cushions, wood panelled wall and soft carpet"></div>
  <div class="back-photo-fade"></div>

  <div class="back-copy">
    <article class="feature">
      <h2 class="feature-title">Reliable:</h2>
      <p class="feature-text">We pride ourselves on providing outstanding services to our customers. From a single carpet or rug, to a whole-house clean, we provide a reliable and friendly service. Call us to discuss your needs.</p>
    </article>
    <article class="feature">
      <h2 class="feature-title">Professional:</h2>
      <p class="feature-text">We use the latest hot water extraction cleaning technology to give us the ability to get into the ground down dirt deep down inside the fibres.</p>
    </article>
    <article class="feature">
      <h2 class="feature-title">Trustworthy:</h2>
      <p class="feature-text">We are fully insured to work in your home, we guarantee all our work so if any issues do arise we will do our upmost to put it back right for you.</p>
    </article>
  </div>

  <p class="back-name">Velvet Nest</p>
  <div class="back-contact-band"></div>
  <p class="contact contact-phone">
    <svg viewBox="0 0 24 24" fill="none" stroke="currentColor" stroke-width="1.6"><circle cx="12" cy="12" r="10.5"/><path d="M8.5 6.5l2 2.2-1.1 1.6c.8 1.7 2 2.9 3.7 3.7l1.6-1.1 2.2 2-1.2 1.8c-4-.6-7.2-3.8-7.8-7.8z"/></svg>
    01632 960 418
  </p>
  <p class="contact contact-email">
    <svg viewBox="0 0 24 24" fill="none" stroke="currentColor" stroke-width="1.6"><circle cx="12" cy="12" r="10.5"/><rect x="6.5" y="8" width="11" height="8"/><path d="M6.5 8l5.5 4.5L17.5 8"/></svg>
    info@velvetnest-clean.co.uk
  </p>
</section>

</body>
</html>
```